Real Estate Company Needs a Contemporary/Modern Business Card Design

We need a Contemporary/Modern Business Card Design for a New Real Estate Company based in San Francisco, CA called Colvane Terrish Realtors. We would like to see designs that use the color red for the "Colvane Terrish" and gold for the "Realtors." The design should communicate being Modern and yet Established and Stable.

Industry/Entity Type

Business

```html
<!DOCTYPE html>
<html lang="en">
<head>
<meta charset="utf-8">
<title>Colvane Terrish Realtors – Business Card</title>
<link href="https://fonts.googleapis.com/css2?family=Exo+2:wght@500;700&family=Open+Sans:wght@400;600;700&display=swap" rel="stylesheet">
<style>
  :root {
    --backdrop: #e9e6e1;
    --card-black: #1c1c1e;
    --band-red: #c8343a;
    --band-red-light: #e35a5a;
    --band-red-dark: #9e2128;
    --gold: #c9a233;
    --gold-light: #f1d77a;
    --text-white: #ffffff;
    --text-soft: #f3dada;
    --brand-red: #e0383e;
    --brand-gold: #d8b347;
  }
  html, body {
    margin: 0;
    width: 1200px;
    height: 891px;
    overflow: hidden;
    background: var(--backdrop);
  }
  .canvas {
    position: relative;
    width: 1200px;
    height: 891px;
  }
  .card {
    position: absolute;
    left: 100px;
    top: 160px;
    width: 1000px;
    height: 572px;
    background: var(--card-black);
    overflow: hidden;
    box-shadow: 0 18px 40px rgba(0,0,0,0.25);
  }
  .card-art {
    position: absolute;
    inset: 0;
  }
  .brand {
    position: absolute;
    left: 90px;
    top: 150px;
    display: flex;
    align-items: center;
    gap: 20px;
  }
  .brand-mark {
    width: 44px;
    height: 44px;
    background: var(--gold);
  }
  .brand-name,
  .brand-suffix {
    font-family: "Exo 2", sans-serif;
    font-weight: 700;
    font-size: 40px;
    line-height: 1.1;
    margin: 0;
  }
  .brand-name { color: var(--brand-red); }
  .brand-suffix { color: var(--brand-gold); }
  .person {
    position: absolute;
    left: 190px;
    top: 368px;
    font-family: "Open Sans", sans-serif;
    color: var(--text-white);
  }
  .person-name {
    margin: 0;
    font-weight: 700;
    font-size: 26px;
    letter-spacing: 0.5px;
  }
  .person-title {
    margin: 2px 0 0;
    font-size: 17px;
    color: var(--text-soft);
  }
  .contact-list {
    position: absolute;
    left: 600px;
    top: 326px;
    margin: 0;
    padding: 0;
    list-style: none;
    font-family: "Open Sans", sans-serif;
    font-size: 16px;
    color: var(--text-white);
  }
  .contact-list li {
    display: flex;
    align-items: center;
    gap: 12px;
    height: 24px;
  }
  .contact-icon {
    width: 15px;
    height: 15px;
    flex: none;
  }
</style>
</head>
<body>
<main class="canvas">
  <section class="card" aria-label="Business card front">
    <svg class="card-art" viewBox="0 0 1000 572" aria-hidden="true">
      <defs>
        <linearGradient id="band-gradient" x1="0" y1="0" x2="1" y2="1">
          <stop offset="0" stop-color="#9e2128"/>
          <stop offset="0.55" stop-color="#e35a5a"/>
          <stop offset="1" stop-color="#c8343a"/>
        </linearGradient>
        <linearGradient id="gold-gradient" x1="0" y1="0" x2="1" y2="0">
          <stop offset="0" stop-color="#c9a233"/>
          <stop offset="0.5" stop-color="#f1d77a"/>
          <stop offset="1" stop-color="#c9a233"/>
        </linearGradient>
      </defs>
      <polygon class="band" points="180,300 1000,300 1000,470 120,470" fill="url(#band-gradient)"/>
      <polygon points="470,300 505,300 470,370 435,370" fill="#1c1c1e"/>
      <polygon points="520,300 545,300 510,370 485,370" fill="#1c1c1e"/>
      <polygon points="460,400 495,400 460,470 425,470" fill="#1c1c1e"/>
      <rect x="40" y="38" width="360" height="16" fill="url(#gold-gradient)"/>
      <rect x="40" y="72" width="250" height="10" fill="url(#gold-gradient)"/>
      <rect x="40" y="38" width="10" height="90" fill="url(#gold-gradient)"/>
      <rect x="720" y="510" width="240" height="10" fill="url(#gold-gradient)"/>
      <rect x="820" y="536" width="140" height="10" fill="url(#gold-gradient)"/>
    </svg>

    <div class="brand">
      <span class="brand-mark" aria-hidden="true"></span>
      <div>
        <p class="brand-name">Colvane Terrish</p>
        <p class="brand-suffix">Realtors</p>
      </div>
    </div>

    <div class="person">
      <p class="person-name">DORIAN KESSEL</p>
      <p class="person-title">Managing Director</p>
    </div>

    <ul class="contact-list">
      <li>
        <svg class="contact-icon" viewBox="0 0 16 16" aria-hidden="true"><rect x="3" y="1" width="10" height="14" rx="2" fill="none" stroke="currentColor" stroke-width="1.6"/></svg>
        015 284 3907
      </li>
      <li>
        <svg class="contact-icon" viewBox="0 0 16 16" aria-hidden="true"><path d="M4 1.5l3 3-1.6 2a9 9 0 0 0 4.1 4.1l2-1.6 3 3-2 2C6.5 14 2 9.5 2 3.5z" fill="currentColor"/></svg>
        015 284 3908
      </li>
      <li>
        <svg class="contact-icon" viewBox="0 0 16 16" aria-hidden="true"><rect x="1" y="3" width="14" height="10" fill="currentColor"/><path d="M1 3l7 6 7-6" fill="none" stroke="#c8343a" stroke-width="1.4"/></svg>
        hello@colvaneterrish.com
      </li>
      <li>
        <svg class="contact-icon" viewBox="0 0 16 16" aria-hidden="true"><circle cx="8" cy="8" r="6.5" fill="none" stroke="currentColor" stroke-width="1.5"/><path d="M1.5 8h13M8 1.5c-3 3.5-3 9.5 0 13M8 1.5c3 3.5 3 9.5 0 13" fill="none" stroke="currentColor" stroke-width="1.2"/></svg>
        www.colvaneterrish.com
      </li>
      <li>
        <svg class="contact-icon" viewBox="0 0 16 16" aria-hidden="true"><path d="M8 15s5-5.2 5-9A5 5 0 0 0 3 6c0 3.8 5 9 5 9z" fill="currentColor"/><circle cx="8" cy="6" r="1.8" fill="#c8343a"/></svg>
        214 Harbor Lane, Suite 9 SF
      </li>
    </ul>
  </section>
</main>
</body>
</html>
```